Etiketten-Design für Imkerei
Zielgruppe
Wir sind eine kleine Imkerei die sich vorwiegend auf Honig konzentriert. Waldhonig und Wald-Blütenhonig .
Zielgruppe sind alle die gerne Qualitätshonig aus der Region kaufen .
Aufgabenstellung
es sind 2 verschiedene Etiketten Größen für verschieden Nettofüllmengen :
250 g - H 3,5 cm ,B 12 cm
500 g - H 5 cm , B 17 cm
Honigsortenbezeichnung je einmal 'Wald' einmal 'Wald-Blüten' sollte aber möglich sein auch andere Honigsorten anzugeben.
die gesetzlichen Vorschriften der Schriftgröße für Adresse, Haltbarkeit und 100% Honig aus Österreich sind 1,2 mm immer vom kleinsten Buchstaben ausgehend . Ausgenommen NETTOFÜLLMENGE muss mind. 4 mm sein auch vom kleinsten Buchstaben ausgehend .
die Adresse und Mindestens Haltbar bis auf der linken Seite der Etikette( muss auf der gleichen Seite stehen) , in der Mitte Schriftzug mit Grafik wobei hier die Größe keiner Vorschrift unterliegt.
Sortenbezeichnung kann in der Mitte sein muss aber nicht und rechts neben Schriftzug „KOLMER`S HONIG“ die Nettofüllmenge , ganz rechts dann 100% Honig aus Österreich
Die Hintergrundfarbe der Etiketten sollten in Granitgrau- Schwarz lebendig also ähnlich wie marmoriert sein.
Schriftzug in der Mitte : ' Kolmer`s Honig ' das 'B' sollte eine Biene sein , den Rest überlasse ich Euch Profis . Schriftfarbe nicht Metallic oder Gold da die Deckel Silber sind. Fotos füge ich unten ein wobei es weder diese Biene sein muss noch der Schriftzug das ist nur ein Beispiel. Das ganze sollte edel und doch verspielt aussehen . Den Schriftzug Kolmer`s Honig möchte ich in weiterer Folge auch alleine verwenden können wie zB. für Rechnungen oder Homepage .
Angaben auf der Etikette wie oben beschrieben:
Imkerei
T & L Wimmerhuber
Tannenhoferweg 214
9734 Lindenau
+436608274316 1,2 mm ausgehend vom kleinsten Buchstaben
Mindestens Haltbar bis:
siehe Glasunterseite
Trocken und vor Wärme geschützt Lagern ! 1,2 mm ausgehend vom kleinsten Buchstaben

```html
<!DOCTYPE html>
<html lang="de">
<head>
<meta charset="utf-8">
<title>Kolmer's Honig – Etikett 500 g</title>
<link rel="stylesheet" href="https://fonts.googleapis.com/css2?family=Poppins:wght@400;500;600&display=swap">
<style>
  :root {
    --stage: #2a2a2a;
    --granite-dark: #1f1f1f;
    --granite-mid: #333333;
    --granite-light: #454545;
    --honey-gold: #f2c21b;
    --honey-deep: #c99a10;
    --text-light: #f4f4f4;
  }
  * { margin: 0; padding: 0; box-sizing: border-box; }
  html, body {
    width: 1200px; height: 1200px; overflow: hidden;
    background: var(--stage);
    font-family: "Poppins", sans-serif;
    color: var(--text-light);
  }
  .label {
    position: absolute; left: 0; top: 423px;
    width: 1200px; height: 354px;
    overflow: hidden;
  }
  .label__granite { position: absolute; inset: 0; }
  .label__band {
    position: absolute; left: 0; width: 100%; height: 18px;
    background: linear-gradient(90deg, var(--honey-deep), var(--honey-gold) 30%, var(--honey-deep) 60%, var(--honey-gold));
  }
  .label__band--top { top: 0; }
  .label__band--bottom { bottom: 0; }

  .producer {
    position: absolute; left: 24px; width: 216px;
    text-align: center; font-size: 14.5px; line-height: 18.6px; font-weight: 400;
  }
  .producer--address { top: 64px; }
  .producer--shelf { top: 206px; }
  .producer__divider {
    position: absolute; left: 24px; top: 181px; width: 216px; height: 1.5px;
    background: var(--honey-gold);
  }

  .brand {
    position: absolute; left: 318px; top: 140px; width: 564px;
    display: flex; align-items: center; justify-content: center; gap: 14px;
  }
  .brand__dot {
    width: 22px; height: 22px; border-radius: 50%; background: var(--honey-gold); flex: none;
  }
  .brand__name {
    font-size: 60px; font-weight: 500; line-height: 1; color: var(--text-light); white-space: nowrap;
  }
  .variety {
    position: absolute; left: 644px; top: 214px; width: 152px; text-align: center;
    font-size: 20px; font-weight: 600;
  }

  .origin {
    position: absolute; left: 956px; top: 116px; width: 216px; height: 32px;
    border: 1.5px solid var(--honey-gold);
    display: flex; align-items: center; justify-content: center;
    font-size: 14.5px;
  }
  .net-label {
    position: absolute; left: 956px; top: 154px; width: 216px; text-align: center;
    font-size: 14.5px;
  }
  .net-amount {
    position: absolute; left: 956px; top: 180px; width: 216px; text-align: center;
    font-size: 34px; font-weight: 500;
  }
</style>
</head>
<body>
  <section class="label">
    <svg class="label__granite" width="1200" height="354" role="img" aria-label="Granitgrau-schwarzer marmorierter Hintergrund mit verschnörkeltem Ornament">
      <defs>
        <radialGradient id="graniteGlow" cx="50%" cy="50%" r="70%">
          <stop offset="0" stop-color="#454545"/>
          <stop offset="0.55" stop-color="#333333"/>
          <stop offset="1" stop-color="#1f1f1f"/>
        </radialGradient>
      </defs>
      <rect width="1200" height="354" fill="url(#graniteGlow)"/>
    </svg>
    <div class="label__band label__band--top"></div>
    <div class="label__band label__band--bottom"></div>

    <p class="producer producer--address">Imkerei<br>T &amp; L Wimmerhuber<br>Tannenhoferweg 214<br>9734 Lindenau<br>+436608274316</p>
    <div class="producer__divider"></div>
    <p class="producer producer--shelf">Mindestens Haltbar bis:<br>siehe Glasunterseite<br>Trocken und vor Wärme<br>geschützt Lagern !</p>

    <div class="brand">
      <span class="brand__dot"></span>
      <span class="brand__name">Kolmer's Honig</span>
    </div>
    <p class="variety">Wald-Blüten</p>

    <p class="origin">100% Honig aus Österreich</p>
    <p class="net-label">Nettofüllmenge:</p>
    <p class="net-amount">500g</p>
  </section>
</body>
</html>
```